Semi Permanent make up flyer

Hi

I will be sending a few thousand flyers dropped door to door in some very lovely parts of London.

The flyer must contain the following information;

New studio in Greenwich

Velmira Lineo trained technician - gold advanced level

Free consultation no obligation

Price List;
Eyebrow hair stroke: £325
Eyebrows 3D effect: £395
Microblading hair stroke: £330
Eyelash enhancement Top: £250
Eyelash enhancement Top & Bottom: £300
Lip blush: £450

Tel;……………….
Facebook: Odelie Permanent Cosmetics
Instagram: Odelie_Permanent_Cosmetics

Special introductory offers - available for a limited time only;
Like & share my page for 10% off any treatment
Refer a friend for £50 off each
Buy one treatment get 50% off another

I would like it to look clean, professional, expensive, and high end/luxury

I’m happy to make this a double sided print so I can have my logo on the front and the information on the back.

It must include my logo.

If you could use images of appealing women I think it would work best. Images have to have nice eyes, lips and brows. Weather you use entire face or features that is up to you.

Please show me a selection of different colour ways across the whole design. I personally feel softer tones would work. No black or bright colours.

I will be getting my new phone number in the next few days. I will let you know via messages what it is for you to add it in.

Any questions feel free to ask.

Target Market(s)

Women

Industry/Entity Type

Beauty Salon

Font styles to use
Sans Serif

Requirements
Must have
• Everything in Description
Nice to have
• The designers give their ideas. Im looking for input
Should not have
• Childish, cheap images or fonts. This is very high end so needs to look it

```html
<!DOCTYPE html>
<html lang="en">
<head>
<meta charset="utf-8">
<title>Odelie Permanent Cosmetics – Flyer</title>
<link rel="stylesheet" href="https://fonts.googleapis.com/css2?family=Raleway:wght@200;300;400;600;700&display=swap">
<style>
  :root {
    --page-bg: #efece8;
    --cream: #f3f0ea;
    --paper: #f6f4ef;
    --gold: #c9a136;
    --gold-soft: #d9bd77;
    --gold-deep: #8a6a22;
    --ink: #2f2a26;
    --ink-soft: #4a4440;
    --skin-light: #e8cfb9;
    --skin-mid: #c9a183;
    --hair-brown: #8a5f45;
    --hair-blonde: #e9dcc4;
    --tile: #a8844a;
  }
  * { box-sizing: border-box; margin: 0; padding: 0; }
  html, body { width: 1200px; height: 1200px; overflow: hidden; }
  body {
    background: var(--page-bg);
    font-family: "Raleway", sans-serif;
    color: var(--ink);
    display: flex;
    align-items: center;
    justify-content: center;
    gap: 60px;
  }
  .flyer {
    position: relative;
    width: 460px;
    height: 960px;
    overflow: hidden;
    box-shadow: 0 6px 22px rgba(60, 50, 40, 0.18);
  }

  /* Front */
  .flyer--front { background: var(--cream); }
  .front-photo {
    position: absolute; inset: 0 0 auto 0; height: 620px;
    background:
      linear-gradient(to bottom, rgba(243,240,234,0) 55%, var(--cream) 100%),
      linear-gradient(100deg, var(--hair-brown) 0%, var(--skin-mid) 22%, var(--skin-light) 50%, var(--skin-mid) 100%);
  }
  .front-lower {
    position: absolute; inset: auto 0 0 0; height: 200px;
    background: linear-gradient(to bottom, var(--cream) 0%, var(--skin-light) 60%, var(--skin-mid) 100%);
  }
  .brand {
    position: absolute; left: 0; right: 0; top: 560px;
    text-align: center;
  }
  .brand__dot {
    width: 54px; height: 54px; border-radius: 50%;
    background: var(--gold);
    margin: 0 auto 40px;
  }
  .brand__name {
    font-size: 30px; font-weight: 300; letter-spacing: 0.62em;
    color: var(--ink-soft); padding-left: 0.62em;
  }
  .brand__tag {
    margin-top: 8px; font-size: 13px; font-weight: 400;
    letter-spacing: 0.22em; color: var(--gold);
  }

  /* Back */
  .flyer--back { background: var(--paper); }
  .back-photo {
    position: absolute; inset: 0 0 auto 0; height: 420px;
    background:
      linear-gradient(to bottom, rgba(246,244,239,0) 45%, var(--paper) 100%),
      linear-gradient(90deg, var(--paper) 0%, var(--hair-blonde) 35%, var(--skin-light) 70%, var(--hair-blonde) 100%);
  }
  .content {
    position: absolute; right: 28px; left: 28px; top: 272px;
    text-align: right;
  }
  .studio {
    font-size: 14px; font-weight: 600; letter-spacing: 0.18em;
    text-transform: uppercase; color: var(--gold-deep); margin-bottom: 10px;
  }
  .headline {
    font-size: 27px; font-weight: 200; line-height: 0.98;
    letter-spacing: -0.02em; color: var(--ink);
  }
  .offers { margin-top: 10px; font-size: 19px; font-weight: 700; line-height: 1.32; }
  .offers p + p { margin-top: 2px; }
  .offer--gold { color: var(--gold); }
  .offer--dark { color: var(--ink); }
  .prices {
    list-style: none; margin-top: 12px;
    font-size: 18px; font-weight: 300; line-height: 1.3; color: var(--ink-soft);
  }
  .prices .price { color: var(--gold-soft); }
  .consult {
    margin-top: 12px; font-size: 16px; font-weight: 600; color: var(--gold);
  }

  .badge {
    position: absolute; left: -40px; top: 400px;
    width: 210px; height: 210px; border-radius: 50%;
    background: radial-gradient(circle at 30% 25%, #4a3a26 0%, #6e5424 45%, var(--gold) 85%);
    display: flex; flex-direction: column; justify-content: center;
    padding-left: 60px; padding-right: 10px;
    text-align: center;
  }
  .badge__title {
    font-size: 20px; font-weight: 200; line-height: 0.98; color: #f6efe0;
  }
  .badge__level {
    margin-top: 4px; font-size: 15px; font-weight: 700;
    letter-spacing: 0.12em; line-height: 1.05; color: var(--gold-soft);
  }

  .contact {
    position: absolute; right: 180px; top: 830px;
    text-align: right; font-size: 14px; font-weight: 300; line-height: 1.45;
  }
  .contact__tel { font-size: 21px; font-weight: 600; margin-bottom: 4px; }
  .contact strong { font-weight: 700; }
  .logo-box {
    position: absolute; right: 30px; top: 790px;
    width: 130px; height: 120px; border-radius: 12px;
    background: var(--tile);
    display: flex; flex-direction: column; align-items: center; justify-content: center;
  }
  .logo-box__name { font-size: 15px; font-weight: 400; letter-spacing: 0.4em; color: var(--paper); padding-left: 0.4em; }
  .logo-box__tag { margin-top: 4px; font-size: 7px; font-weight: 400; letter-spacing: 0.14em; color: var(--paper); }
</style>
</head>
<body>

<section class="flyer flyer--front">
  <div class="front-photo" role="img" aria-label="Close-up photograph of a woman's lips and chin with softly flowing brown hair"></div>
  <div class="front-lower" role="img" aria-label="Soft-focus photograph of flowing brown hair and shoulder"></div>
  <div class="brand">
    <div class="brand__dot"></div>
    <div class="brand__name">ODELIE</div>
    <div class="brand__tag">PERMANENT COSMETICS</div>
  </div>
</section>

<section class="flyer flyer--back">
  <div class="back-photo" role="img" aria-label="Bright portrait photograph of a woman with wavy blonde hair and defined brows and eyes"></div>

  <div class="badge">
    <div class="badge__title">VELMIRA<br>LINEO<br>TRAINED<br>TECHNICIAN</div>
    <div class="badge__level">Gold<br>Advanced<br>Level</div>
  </div>

  <div class="content">
    <p class="studio">New studio in Greenwich</p>
    <h1 class="headline">Special introductory<br>offers available for<br>a limited time only</h1>
    <div class="offers">
      <p class="offer--gold">Like &amp; share my page for<br>10% off any treatment</p>
      <p class="offer--dark">Refer a friend for<br>£50 off each</p>
      <p class="offer--gold">Buy one treatment<br>get 50% off another</p>
    </div>
    <ul class="prices">
      <li>Lip blush: <span class="price">£450</span></li>
      <li>Eyebrow hair stroke: <span class="price">£325</span></li>
      <li>Eyebrows 3D effect: <span class="price">£395</span></li>
      <li>Microblading hair stroke: <span class="price">£330</span></li>
      <li>Eyelash enhancement Top: <span class="price">£250</span></li>
      <li>Eyelash enhancement Top &amp; Bottom: <span class="price">£300</span></li>
    </ul>
    <p class="consult">Free consultation – no obligation</p>
  </div>

  <div class="contact">
    <div class="contact__tel">Tel: 01632 960 418</div>
    <div><strong>Facebook:</strong> Odelie Permanent Cosmetics</div>
    <div><strong>Instagram:</strong> Odelie_Permanent_Cosmetics</div>
  </div>

  <div class="logo-box">
    <div class="logo-box__name">ODELIE</div>
    <div class="logo-box__tag">PERMANENT COSMETICS</div>
  </div>
</section>

</body>
</html>
```